Wine Bottle Label Logo Design

My fiancé and I are getting married in September and we made homemade wine which will be given to the guests as a wedding favor. We need label/logo for our wine bottles. We were looking for something rustic yet modern and simple. We had an idea for beige and cranberry colored wine stained, weathered, imperfect heart. Things that will need to be incorporated into the label design are as follows:
Our last name and also the name of the wine: Fusaldi
The year: 2012
Where is says Alcohol Content on a wine bottle normally write: Alcohol: Deceiving% by vol.
Type of wine: Red Wine
Incorporate our wedding date: Foot Stomped and Bottled for Nadia and Gus's Wedding Day 9/28/13
Wedding

```html
<!DOCTYPE html>
<html lang="en">
<head>
<meta charset="utf-8">
<title>Fusaldi Red Wine 2012 – Wedding Label</title>
<link href="https://fonts.googleapis.com/css2?family=Pinyon+Script&family=Cinzel:wght@400;600&family=Cormorant+Garamond:wght@500;600&display=swap" rel="stylesheet">
<style>
  :root {
    --backdrop: #2a2624;
    --label-core: #b0655a;
    --label-mid: #94443c;
    --label-edge: #5e1a18;
    --gold: #e3d08e;
    --wine-red: #9c1414;
    --ink-dark: #2b1110;
    --ink-light: #f3e6d6;
    --sketch-tone: #c79a88;
    --ring-tone: #d2ad4c;
  }
  html, body {
    margin: 0;
    padding: 0;
    width: 789px;
    height: 1200px;
    overflow: hidden;
    background: var(--backdrop);
  }
  .canvas {
    position: relative;
    width: 789px;
    height: 1200px;
    display: flex;
    align-items: center;
    justify-content: center;
  }
  .wine-label {
    position: relative;
    width: 430px;
    height: 660px;
    border-radius: 14px;
    background: radial-gradient(ellipse at 50% 45%, var(--label-core) 0%, var(--label-mid) 55%, var(--label-edge) 100%);
    box-shadow: 0 10px 40px rgba(0,0,0,0.5);
    overflow: hidden;
    text-align: center;
  }
  .label-sketch {
    position: absolute;
    left: 70px;
    top: 200px;
    width: 290px;
    height: 200px;
    border-radius: 50%;
    background: radial-gradient(ellipse at center, var(--sketch-tone) 0%, rgba(199,154,136,0) 72%);
    opacity: 0.7;
  }
  .monogram {
    position: absolute;
    top: 46px;
    left: 0;
    right: 0;
    display: flex;
    align-items: center;
    justify-content: center;
    gap: 12px;
  }
  .monogram-dot {
    width: 14px;
    height: 14px;
    border-radius: 50%;
    background: var(--gold);
  }
  .monogram-initials {
    font-family: "Pinyon Script", cursive;
    font-size: 64px;
    color: var(--gold);
    line-height: 1;
  }
  .wine-name {
    position: absolute;
    top: 178px;
    left: 0;
    right: 0;
    font-family: "Pinyon Script", cursive;
    font-size: 118px;
    line-height: 1;
    color: var(--gold);
  }
  .wedding-rings {
    position: absolute;
    top: 330px;
    left: 160px;
    width: 120px;
    height: 70px;
    border-radius: 40%;
    background: radial-gradient(ellipse at center, var(--ring-tone) 0%, rgba(210,173,76,0.3) 60%, rgba(210,173,76,0) 100%);
  }
  .wine-type {
    position: absolute;
    top: 420px;
    left: 0;
    right: 0;
    font-family: "Pinyon Script", cursive;
    font-size: 58px;
    line-height: 1;
    color: var(--wine-red);
  }
  .vintage {
    position: absolute;
    top: 486px;
    left: 0;
    right: 0;
    font-family: "Cinzel", serif;
    font-weight: 400;
    font-size: 40px;
    color: var(--ink-dark);
    letter-spacing: 1px;
  }
  .label-details {
    position: absolute;
    top: 548px;
    left: 30px;
    right: 30px;
    font-family: "Cormorant Garamond", serif;
    font-weight: 600;
    font-size: 20px;
    line-height: 1.15;
    color: var(--ink-light);
  }
  .label-details p { margin: 0; }
</style>
</head>
<body>
<main class="canvas">
  <section class="wine-label">
    <div class="label-sketch" role="img" aria-label="Faded sketch of grape harvest scene behind the name"></div>
    <div class="monogram">
      <span class="monogram-dot"></span>
      <span class="monogram-initials">N&amp;G</span>
    </div>
    <h1 class="wine-name" style="margin:0;font-weight:400;">Fusaldi</h1>
    <div class="wedding-rings" role="img" aria-label="Illustration of two interlocked gold wedding rings"></div>
    <h2 class="wine-type" style="margin:0;font-weight:400;">Red Wine</h2>
    <div class="vintage">2012</div>
    <div class="label-details">
      <p>Alcohol: Deceiving% by vol.</p>
      <p>Foot stomped and bottled for</p>
      <p>Nadia and Gus's Wedding Day 9/28/13</p>
    </div>
  </section>
</main>
</body>
</html>
```